Quiet Ledger needs a book cover

Enabling people to find a new way of looking at money. If peoples thoughts, attitude and emotions around money are not inline with their goals and dreams then it is often harder to achieve their version of success.

Recognition that we have an emotional and a practical way with money.

Quiet Ledger enables people to find a sustainable (balanced) way with money for their life right now and their future.

Developing this over the years and seeing clients achieve a clear picture/idea/thought connection that is positive around money and it's purpose to them in their lives has truly been fabulous as they have then gone on to achieve their goals and dreams.

Title of book = Quiet Ledger
Tag line = Being healthy being wealthy
Authors Name = Ruth Pell
Book Size = 135 width x 185 height
Thumbnail = Cover must work well as well as full size
Looking for simple and clear app-able / icon type image
Feel free to have fun with it
A simple yet refreshing balanced, eye-catching design.

The back will include authors photo, blurb, testimonials, barcode, ISBN number & price. I will provide once front cover is sorted.

Reason: Realised that the tag line for the book was incorrect.

Target Market(s)

Individuals

Industry/Entity Type

Work

Requirements
Must have
• First work on front cover, once approved we can then do spine and back cover

```html
<!DOCTYPE html>
<html lang="en">
<head>
<meta charset="utf-8">
<title>Quiet Ledger — Book Cover</title>
<link href="https://fonts.googleapis.com/css2?family=Bebas+Neue&family=Roboto+Condensed:wght@700&family=Montserrat:wght@300&display=swap" rel="stylesheet">
<style>
  :root {
    --cover-bg: #ffffff;
    --bubble-red: #c80000;
    --bubble-text: #ffffff;
    --ink: #111111;
    --icon-fill: #ececec;
  }
  html, body {
    margin: 0;
    padding: 0;
    overflow: hidden;
    background: var(--cover-bg);
  }
  .cover {
    position: relative;
    width: 875px;
    height: 1200px;
    background: var(--cover-bg);
    overflow: hidden;
  }
  .speech-bubble {
    position: absolute;
    left: 0;
    top: 0;
  }
  .speech-bubble path {
    fill: var(--bubble-red);
  }
  .title-block {
    position: absolute;
    left: 33px;
    top: 33px;
    width: 811px;
    text-align: center;
    color: var(--bubble-text);
  }
  .book-title {
    margin: 0;
    padding-top: 66px;
    font-family: "Bebas Neue", "Oswald", sans-serif;
    font-weight: 400;
    font-size: 134px;
    line-height: 1;
    letter-spacing: 1px;
  }
  .book-tagline {
    margin: 2px 0 0;
    font-family: "Roboto Condensed", "Arial Narrow", sans-serif;
    font-weight: 700;
    font-size: 52px;
    line-height: 54px;
  }
  .piggy-icon {
    position: absolute;
    left: 181px;
    top: 632px;
    width: 451px;
    height: 320px;
    background: var(--icon-fill);
    border-radius: 40%;
  }
  .author-name {
    position: absolute;
    left: 0;
    top: 1052px;
    width: 875px;
    margin: 0;
    text-align: center;
    font-family: "Montserrat", "Helvetica Neue", sans-serif;
    font-weight: 300;
    font-size: 70px;
    line-height: 1;
    letter-spacing: 6px;
    color: var(--ink);
  }
</style>
</head>
<body>
  <main class="cover">
    <svg class="speech-bubble" width="875" height="620" viewBox="0 0 875 620" aria-hidden="true">
      <path d="M48 33 H829 Q844 33 844 48 V400 Q844 415 829 415 H670 L445 594 L560 415 H48 Q33 415 33 400 V48 Q33 33 48 33 Z"/>
    </svg>
    <header class="title-block">
      <h1 class="book-title">QUIET LEDGER</h1>
      <p class="book-tagline">Being healthy<br>being wealthy</p>
    </header>
    <div class="piggy-icon" role="img" aria-label="Simple black line icon of a piggy bank with a coin slot and curly tail"></div>
    <p class="author-name">RUTH PELL</p>
  </main>
</body>
</html>
```